Create a Brochure Design for Harlow Senior Living

Harlow Senior Living is a subsidiary of the Harlow Care Group. This brochure is specifically for the Harlow Senior Living company and brand. Create a 3 panel, front and back, tri-fold brochure. This brochure will be a way to introduce our senior living care home to the community, prospective, clients, and various referral partners. It is modern and state of the art home. Like the home, the brochure must be eye catching, unique in its deliverables (as it doesn’t feel like a care facility) and demonstrate both attention to detail and comfort. Our organization is sophisticated and built around warmth, care and individualized personal attention. The most important aspect of this design is to focus on creating a nurturing, warm, and inviting feel where you would want to put your own loved ones in our care home.
I am open to the creativity of the designer to develop something based on the above criteria; however I would like the design to work well with the existing collateral material. What I mean by that is that while I want everything to have its own personality and stand out as its own brand representative, I still need to be able to tell that the overall design concept stays stylistically inside of the same ‘family’ of existing designed material. Because of this, below I would like for the designer to pull inspiration from the link to our website (Located below) as well as from the attachment of our recently refreshed business cards (Attached). This should allow each design to be unique and creative, while still staying inside of a framework and the feel/style that I am looking for.
Finally, I want all the designers to understand that this brochure design is for a facility where we are responsible to provide care for active, positive, and happy seniors/elders. We have care professionals and staff on-site to provide 24x7, around the clock, care to the elders and geriatric residents as it is needed and required. The photos that are used must represent aging gracefully and with elegance.
Target Market(s)
Seniors(50+), Caring Family Members, Social Workers, Physicians, Hospitals
Industry/Entity Type
Business
Requirements
Must have
- • The company logo must be included.
Nice to have
- Attached you will find a sampling of images related to the long term care industry. Please feel free to use your own images as you see fit. The interior care home pictures are of our actual facility and should be incorporated into the brochure and your design.
Company Information
• Look under the Harlow Senior Living tab at
www.harlowcaregroup.example.

```html
<!DOCTYPE html>
<html lang="en">
<head>
<meta charset="utf-8">
<title>Harlow Senior Living – Brochure Inside Spread</title>
<link rel="stylesheet" href="https://fonts.googleapis.com/css2?family=Arimo:wght@400&family=Playball&family=Tinos&display=swap">
<style>
  :root{
    --bg:#a8d2d5;
    --panel-dark:#5b9d9c;
    --panel-mid:#71aeb0;
    --panel-right:#5f9f9d;
    --text:#ffffff;
    --quote:#f4efdc;
    --room-warm:#b48e5e;
    --room-deep:#6e5036;
  }
  *{margin:0;padding:0;box-sizing:border-box}
  html,body{width:1200px;height:848px;overflow:hidden;background:var(--bg)}
  .spread{position:relative;width:1200px;height:848px;background:var(--bg);font-family:"Arimo",Arial,sans-serif;color:var(--text)}
  .photo{position:absolute;top:0;height:299px}
  .photo-lounge{left:0;width:399px;background:linear-gradient(160deg,#e7d2a6 0%,#a98458 45%,#7a5a3c 100%)}
  .photo-suite{left:417px;width:783px;background:linear-gradient(100deg,#3a2a20 0%,#e9d8a8 35%,#c9a070 60%,#9fbf8c 85%,#e8dcb8 100%)}
  .shapes{position:absolute;inset:0}
  .copy{position:absolute;font-size:15.5px;line-height:22.5px}
  .intro{left:43px;top:420px;width:335px}
  .intro p{margin-bottom:22px}
  .lifestyle{left:463px;top:345px;width:320px}
  .personal{left:878px;top:425px;width:290px}
  .script-heading{font-family:"Playball",cursive;font-size:27px;line-height:30px;font-weight:400}
  .fee-list{list-style:none}
  .lifestyle .script-heading + p{margin-bottom:16px}
  .quote{position:absolute;left:862px;top:688px;width:310px;text-align:center;font-family:"Tinos",serif;font-size:32px;line-height:36px;color:var(--quote)}
</style>
</head>
<body>
<div class="spread">
  <div class="photo photo-lounge" role="img" aria-label="Photo of the home's spacious lounge with sectional sofa and dining area"></div>
  <div class="photo photo-suite" role="img" aria-label="Photo of a resident suite with bed, dressers and a balcony door"></div>

  <svg class="shapes" width="1200" height="848" viewBox="0 0 1200 848" aria-hidden="true">
    <path d="M0 290 C120 340 260 330 399 300 L417 300 L417 320 L0 340 Z" fill="var(--bg)"/>
    <path d="M815 300 C930 325 1060 315 1200 290 L1200 320 L815 320 Z" fill="var(--bg)"/>
    <path d="M0 380 C110 350 250 338 399 362 L399 820 L0 820 Z" fill="var(--panel-dark)"/>
    <rect x="417" y="311" width="398" height="509" fill="var(--panel-mid)"/>
    <path d="M834 373 C960 366 1090 348 1200 300 L1200 832 C1090 842 960 832 834 822 Z" fill="var(--panel-right)"/>
  </svg>

  <div class="copy intro">
    <p>Harlow Senior Living is a unique care concept, designed around a social model which encourages “neighbors” to be as independent as possible, actively participate in life here, and interact with their fellow neighbors.</p>
    <p>Here, you’ll maintain purpose in life while having personal care assistance as needed, activities, exercise, transportation, and companionship. Professional staff will be in residence 24 hours a day. This is a very special home, offering you a loving and nurturing life experience.</p>
  </div>

  <div class="copy lifestyle">
    <h2 class="script-heading">Lifestyle Support</h2>
    <p>For neighbors who are relatively independent but might benefit from lifestyle support, with assistance as needed, medication management, access to staff 24/7, and regular nursing visits.</p>
    <h2 class="script-heading">Monthly fees include:</h2>
    <ul class="fee-list">
      <li>3 daily meals + snacks</li>
      <li>Activities</li>
      <li>Laundry</li>
      <li>Housekeeping</li>
      <li>Utilities</li>
      <li>Accommodations</li>
      <li>Medication Management</li>
      <li>Care Planning</li>
      <li>Regular Nursing Visits</li>
      <li>Access to Staff 24/7</li>
    </ul>
  </div>

  <div class="copy personal">
    <h2 class="script-heading">Personal Care</h2>
    <p>Hands-on care: Daily bathing, dressing, toileting, incontinence care, grooming, assistance with ambulation, transfers, range of motion exercises, verbal cueing, medication management, &amp; feeding.</p>
  </div>

  <p class="quote">”Just bring your suitcase we take care of the rest”</p>
</div>
</body>
</html>
```